Personal Motivational Quote Poster Design

I would like to create a poster with some of my favorite quotes to hang in my office. I did similar projects in 2012 and 2014. I've uploaded the winning designs so you can get a better idea of what I'm looking for. I will provide feedback on your design within 24 hours of receiving it.

The poster must contain the following quotes:

“What the pupil must learn, if he learns anything at all, is that the world will do most of the work for you, provided you cooperate with it by identifying how it really works and aligning with those realities. If we do not let the world teach us, it teaches us a lesson.” - Walter Brindley

“I tackle every big new problem by asking two questions: Who has dealt with this problem well? And what can we learn from them?” - Hal Porter

“If we can really understand the problem, the answer will come out of it, because the answer is not separate from the problem.” - Ravel Ondashanti

“Success is nothing more than a few simple disciplines, practiced every day; while failure is simply a few errors in judgment, repeated every day. It is the accumulative weight of our disciplines and our judgments that leads us to either fortune or failure.” - Ned Calve

“Inaction breeds doubt and fear. Action breeds confidence and courage.” - Rex Halloway

“What’s the one thing you can do, such that by doing it, everything else will be easier or unnecessary?” - Lyle Danvers

Requirements
Must have
• The poster will be 24" high x 36" long and printed on canvas, so the image you create needs to have a resolution of at least 2700 x 3900.
Nice to have
• I don't have an exact vision for how the poster should look, so I am totally open to you using your creativity to develop, arrange and present the content as you'd like.

That said, I would like an image (photo or posterized image) of the person being quoted along with each quote. I do not have specific images that I would like you to use, so you will need to find the images on your own.

The images don't need to be perfect... I am more interested in the poster relating the essence of the quotes and the people being quoted than I am in perfect photographic images of the people being quoted.

```html
<!DOCTYPE html>
<html lang="en">
<head>
<meta charset="utf-8">
<title>Quote Poster</title>
<link rel="stylesheet" href="https://fonts.googleapis.com/css2?family=Montserrat:wght@300;400;600;700&display=swap">
<style>
  :root {
    --paper: #e7e7ea;
    --sky: #22abe3;
    --sky-soft: #bfe4f5;
    --sky-ink: #1785c2;
    --magenta: #e0239a;
    --magenta-soft: #f3b6dc;
    --magenta-ink: #b1177f;
    --lime: #b4cc45;
    --lime-soft: #e1ecb4;
    --lime-ink: #4fa88a;
    --tangerine: #e57e2a;
    --tangerine-soft: #f5d2b3;
    --tangerine-ink: #d26b6e;
    --navy: #2c3f8f;
    --navy-soft: #b9c2e2;
    --navy-ink: #aab8ea;
    --vermilion: #e1442a;
    --vermilion-soft: #f6c8b9;
    --vermilion-ink: #c01f45;
    --ink-light: #ffffff;
  }
  * { margin: 0; padding: 0; box-sizing: border-box; }
  html, body { width: 1200px; height: 900px; overflow: hidden; }
  body {
    background: var(--paper);
    font-family: "Montserrat", sans-serif;
    color: var(--ink-light);
  }
  .poster { position: relative; width: 1200px; height: 900px; overflow: hidden; }
  .panels { position: absolute; inset: 0; }
  .portrait { position: absolute; border-radius: 40% 40% 6px 6px; }
  .quote {
    position: absolute;
    font-weight: 300;
    font-size: 18px;
    line-height: 25px;
  }
  .quote b { font-weight: 600; }
  .author {
    display: block;
    margin-top: 20px;
    font-weight: 700;
    font-size: 16px;
  }
  .quote--sky { left: 104px; top: 77px; width: 440px; }
  .quote--sky .author { color: var(--sky-ink); margin-top: 22px; }
  .quote--magenta { left: 52px; top: 444px; width: 560px; }
  .quote--magenta .author { color: var(--magenta-ink); margin-top: 20px; }
  .quote--lime { left: 63px; top: 679px; width: 440px; }
  .quote--lime .author { color: var(--lime-ink); margin-top: 20px; }
  .quote--tangerine { left: 671px; top: 90px; width: 450px; }
  .quote--tangerine .author { color: var(--tangerine-ink); margin-top: 30px; }
  .quote--navy { left: 693px; top: 440px; width: 440px; font-size: 19px; line-height: 26px; }
  .quote--navy .author { color: var(--navy-ink); margin-top: 18px; }
  .quote--vermilion { left: 679px; top: 677px; width: 380px; }
  .quote--vermilion .author { color: var(--vermilion-ink); margin-top: 22px; }
</style>
</head>
<body>
<main class="poster">
  <svg class="panels" width="1200" height="900" viewBox="0 0 1200 900" aria-hidden="true">
    <polygon points="40,370 628,332 625,676 22,600" fill="var(--magenta-soft)"/>
    <polygon points="34,379 625,339 617,664 16,591" fill="var(--magenta)"/>
    <polygon points="96,18 566,34 628,404 40,340" fill="var(--sky-soft)"/>
    <polygon points="82,9 546,26 621,419 25,349" fill="var(--sky)"/>
    <polygon points="46,616 600,646 614,860 40,884" fill="var(--lime-soft)"/>
    <polygon points="52,606 603,635 611,849 31,874" fill="var(--lime)"/>
    <polygon points="612,58 1176,38 1195,378 616,392" fill="var(--tangerine-soft)"/>
    <polygon points="627,48 1162,26 1187,387 625,376" fill="var(--tangerine)"/>
    <polygon points="640,404 1190,394 1190,712 644,582" fill="var(--navy-soft)"/>
    <polygon points="648,398 1181,386 1181,701 652,574" fill="var(--navy)"/>
    <polygon points="630,616 1190,716 1204,856 690,882 626,650" fill="var(--vermilion-soft)"/>
    <polygon points="623,622 1181,711 1195,849 682,874 618,655" fill="var(--vermilion)"/>
  </svg>

  <div class="portrait" role="img" aria-label="Posterized portrait of Walter Brindley" style="left:430px;top:240px;width:160px;height:148px;background:linear-gradient(180deg,rgba(20,110,170,.35),rgba(20,110,170,.6));"></div>
  <div class="portrait" role="img" aria-label="Posterized portrait of Hal Porter" style="left:440px;top:486px;width:110px;height:130px;background:linear-gradient(180deg,rgba(140,10,90,.3),rgba(140,10,90,.55));"></div>
  <div class="portrait" role="img" aria-label="Posterized portrait of Ravel Ondashanti" style="left:440px;top:682px;width:112px;height:160px;background:linear-gradient(180deg,rgba(90,110,30,.3),rgba(90,110,30,.5));"></div>
  <div class="portrait" role="img" aria-label="Posterized portrait of Ned Calve" style="left:975px;top:232px;width:170px;height:136px;background:linear-gradient(180deg,rgba(150,70,20,.3),rgba(150,70,20,.55));"></div>
  <div class="portrait" role="img" aria-label="Posterized portrait of Rex Halloway" style="left:1000px;top:492px;width:130px;height:156px;background:linear-gradient(180deg,rgba(15,25,80,.35),rgba(15,25,80,.6));"></div>
  <div class="portrait" role="img" aria-label="Posterized portrait of Lyle Danvers" style="left:1020px;top:706px;width:130px;height:136px;background:linear-gradient(180deg,rgba(130,25,15,.3),rgba(130,25,15,.55));"></div>

  <p class="quote quote--sky">What the pupil <b>must learn</b>, if he learns anything at all, is that <b>the world will do most of the work for you</b>, provided you cooperate with it by identifying <b>how it really works</b> and aligning with those realities.<br>If we do not let the <b>world teach us</b>, it teaches us a lesson.<span class="author">Walter Brindley</span></p>

  <p class="quote quote--magenta">I tackle every big new problem by <b>asking two questions:</b><br><b>Who</b> has dealt with this problem well?<br>And <b>what</b> can we learn from them?<span class="author">Hal Porter</span></p>

  <p class="quote quote--lime">If we can <b>really understand</b> the problem,<br>the answer will come out of it,<br>because <b>the answer is not<br>separate from the problem.</b><span class="author">Ravel Ondashanti</span></p>

  <p class="quote quote--tangerine"><b>Success</b> is nothing more than a few simple disciplines, <b>practiced every day;</b> while <b>failure</b> is simply a few errors in judgment, repeated every day. It is the <b>accumulative weight</b> of our disciplines and our judgments that <b>leads us to either fortune or failure.</b><span class="author">Ned Calve</span></p>

  <p class="quote quote--navy"><b>Inaction</b> breeds <b>doubt and fear.</b><br><b>Action</b> breeds <b>confidence and courage.</b><span class="author">Rex Halloway</span></p>

  <p class="quote quote--vermilion">What’s the one thing <b>you can do</b>,<br>such that by doing it, everything<br>else will be <b>easier or unnecessary?</b><span class="author">Lyle Danvers</span></p>
</main>
</body>
</html>
```